Tervoni hd highway sign

would like a comercial truck in backround, and would like it very easy to read. Must have company name Tervoni H.D. Mechanical
would like address included 5142 larkfield frontage road. would a some bullet points on sign
-Commercial truck and trailer inspection and repair
-Heavy equipment repair
-24/7 Mobile service

```html
<!DOCTYPE html>
<html lang="en">
<head>
<meta charset="utf-8">
<title>Tervoni H.D. Mechanical – Highway Sign</title>
<link rel="stylesheet" href="https://fonts.googleapis.com/css2?family=Poppins:wght@600;700;800&display=swap">
<style>
  :root {
    --red-deep: #a3000e;
    --red-bright: #e2001a;
    --white: #ffffff;
    --yellow: #fff21f;
    --navy: #1b1838;
    --sky: #8fa7bd;
    --truck-red: #c8101c;
    --road: #5b5a5e;
  }
  * { margin: 0; padding: 0; box-sizing: border-box; }
  html, body { width: 1200px; height: 403px; overflow: hidden; background: var(--white); }
  .sign {
    position: relative;
    width: 1200px;
    height: 403px;
    overflow: hidden;
    font-family: "Poppins", sans-serif;
    background: linear-gradient(90deg, var(--red-deep) 0%, var(--red-bright) 55%, var(--red-bright) 100%);
  }
  .truck-photo {
    position: absolute;
    inset: 0;
    width: 1200px;
    height: 403px;
  }
  .company-name {
    position: absolute;
    left: 36px;
    top: 14px;
    color: var(--white);
    font-weight: 800;
    font-size: 88px;
    line-height: 82px;
    letter-spacing: 0.5px;
    text-transform: uppercase;
  }
  .contact {
    position: absolute;
    left: 37px;
    display: flex;
    align-items: center;
    height: 42px;
    padding: 0 22px 0 6px;
    border-radius: 21px;
    background: var(--yellow);
    color: var(--navy);
    font-weight: 600;
    font-size: 28px;
    line-height: 1;
  }
  .contact--phone { top: 202px; width: 264px; }
  .contact--address { top: 259px; width: 485px; }
  .contact__icon {
    width: 34px;
    height: 34px;
    margin-right: 12px;
    flex: none;
  }
  .services {
    position: absolute;
    left: 41px;
    top: 316px;
    list-style: none;
    color: var(--white);
    font-weight: 600;
    font-size: 17px;
    line-height: 24.5px;
  }
  .services li { position: relative; padding-left: 22px; }
  .services li::before {
    content: "";
    position: absolute;
    left: 0;
    top: 9px;
    width: 8px;
    height: 8px;
    border-radius: 50%;
    background: var(--yellow);
  }
</style>
</head>
<body>
<main class="sign">
  <svg class="truck-photo" viewBox="0 0 1200 403" role="img" aria-label="Photo of a red semi truck with a silver trailer on a highway under a clear sky">
    <defs>
      <linearGradient id="photoTone" x1="0" y1="0" x2="0.3" y2="1">
        <stop offset="0" stop-color="var(--sky)"/>
        <stop offset="0.3" stop-color="var(--truck-red)"/>
        <stop offset="0.75" stop-color="var(--truck-red)"/>
        <stop offset="1" stop-color="var(--road)"/>
      </linearGradient>
    </defs>
    <path d="M694 0 Q800 190 672 403 L1200 403 L1200 0 Z" fill="url(#photoTone)" stroke="var(--white)" stroke-width="6"/>
  </svg>

  <h1 class="company-name">Tervoni H.D.<br>Mechanical</h1>

  <div class="contact contact--phone">
    <svg class="contact__icon" viewBox="0 0 34 34" aria-hidden="true">
      <circle cx="17" cy="17" r="15" fill="none" stroke="var(--navy)" stroke-width="2.5"/>
      <path d="M11.5 9.5l3 -0.5 1.6 3.8-1.9 1.4a9 9 0 0 0 4.6 4.6l1.4-1.9 3.8 1.6-0.5 3a2 2 0 0 1-2 1.5A12 12 0 0 1 10 11.5a2 2 0 0 1 1.5-2z" fill="none" stroke="var(--navy)" stroke-width="2" stroke-linejoin="round"/>
      <path d="M19 9.5a5.5 5.5 0 0 1 5.5 5.5M19 6.5a8.5 8.5 0 0 1 8.5 8.5" fill="none" stroke="var(--navy)" stroke-width="1.8" stroke-linecap="round"/>
    </svg>
    <span>250 555 0147</span>
  </div>

  <div class="contact contact--address">
    <svg class="contact__icon" viewBox="0 0 34 34" aria-hidden="true">
      <circle cx="17" cy="17" r="15" fill="none" stroke="var(--navy)" stroke-width="2.5"/>
      <path d="M17 26s-6.5-6.8-6.5-11.5a6.5 6.5 0 0 1 13 0C23.5 19.2 17 26 17 26z" fill="var(--navy)"/>
      <circle cx="17" cy="14.5" r="2.4" fill="var(--yellow)"/>
    </svg>
    <span>5142 larkfield frontage road</span>
  </div>

  <ul class="services">
    <li>Commercial truck and trailer inspection and repair</li>
    <li>Heavy equipment repair</li>
    <li>24/7 Mobile service</li>
  </ul>
</main>
</body>
</html>
```